KORBALT

The business want a professional looking business card. We have a scetch we will add but want the extra upgrade, and would like more suggestions for variations of our business cards.

```html
<!DOCTYPE html>
<html lang="en">
<head>
<meta charset="UTF-8">
<title>KORBALT Business Card</title>
<link href="https://fonts.googleapis.com/css2?family=Montserrat:wght@400;500;700&display=swap" rel="stylesheet">
<style>
  :root{
    --bg:#2b2b2b;
    --cream:#f3efe8;
    --sand:#d9c29a;
    --gold:#bf9647;
    --bronze:#7a5522;
    --ink:#6e4a16;
    --ink-soft:#8a6327;
  }
  html,body{margin:0;padding:0;overflow:hidden;}
  body{width:1200px;height:875px;background:var(--bg);position:relative;font-family:"Montserrat",sans-serif;}
  .card{
    position:absolute;width:560px;height:320px;border-radius:22px;
    background:linear-gradient(105deg,var(--cream) 0%,var(--sand) 35%,var(--gold) 68%,var(--bronze) 100%);
    box-shadow:0 18px 40px rgba(0,0,0,.45);overflow:hidden;
  }
  .card--front{left:70px;top:90px;}
  .card--back{left:570px;top:465px;}

  .brand{position:absolute;display:flex;flex-direction:column;align-items:center;color:var(--ink);}
  .brand__row{display:flex;align-items:center;gap:12px;}
  .brand__dot{width:14px;height:14px;border-radius:50%;background:var(--ink);}
  .brand__name{font-weight:500;letter-spacing:.32em;}
  .brand__since{font-weight:500;letter-spacing:.45em;}

  .card--front .brand{left:0;right:0;top:118px;}
  .card--front .brand__name{font-size:40px;}
  .card--front .brand__since{font-size:12px;margin-top:8px;}

  .card--back .brand{right:30px;top:42px;}
  .card--back .brand__name{font-size:22px;}
  .card--back .brand__dot{width:9px;height:9px;}
  .card--back .brand__since{font-size:7px;margin-top:5px;}

  .rule{position:absolute;left:250px;right:28px;top:118px;height:1px;background:var(--ink-soft);opacity:.8;}

  .person{position:absolute;left:40px;top:150px;color:var(--ink);}
  .person__name{font-size:22px;font-weight:700;margin:0;}
  .person__title{font-size:15px;font-weight:400;margin:2px 0 0;}
  .person__rule{width:150px;height:1px;background:var(--ink-soft);margin-top:12px;}

  .contacts{position:absolute;left:40px;top:230px;margin:0;padding:0;list-style:none;color:var(--ink);}
  .contacts li{display:flex;align-items:center;gap:10px;font-size:15px;height:24px;}
  .contacts svg{width:13px;height:13px;fill:var(--ink);flex:none;}
</style>
</head>
<body>

<section class="card card--front" aria-label="Card front">
  <div class="brand">
    <div class="brand__row"><span class="brand__dot"></span><span class="brand__name">KORBALT</span></div>
    <span class="brand__since">SINCE 2026</span>
  </div>
</section>

<section class="card card--back" aria-label="Card back">
  <div class="brand">
    <div class="brand__row"><span class="brand__dot"></span><span class="brand__name">KORBALT</span></div>
    <span class="brand__since">SINCE 2026</span>
  </div>
  <div class="rule"></div>

  <div class="person">
    <p class="person__name">Lars Eikrem Dahl</p>
    <p class="person__title">CEO &amp; Founder</p>
    <div class="person__rule"></div>
  </div>

  <ul class="contacts">
    <li>
      <svg viewBox="0 0 24 24"><path d="M6.6 10.8a15 15 0 0 0 6.6 6.6l2.2-2.2c.3-.3.7-.4 1-.2 1.1.4 2.3.6 3.6.6.6 0 1 .4 1 1V20c0 .6-.4 1-1 1A17 17 0 0 1 3 4c0-.6.4-1 1-1h3.5c.6 0 1 .4 1 1 0 1.3.2 2.5.6 3.6.1.3 0 .7-.2 1z"/></svg>
      004791234567
    </li>
    <li>
      <svg viewBox="0 0 24 24"><path d="M2 5h20v14H2z M4 7v.5l8 5 8-5V7l-8 5z" fill-rule="evenodd"/></svg>
      korbalt.llc@mailhub.com
    </li>
    <li>
      <svg viewBox="0 0 24 24"><circle cx="12" cy="12" r="10" fill="none" stroke="currentColor"/><path d="M12 2a10 10 0 1 0 0 20 10 10 0 0 0 0-20zm0 2c1.5 1.8 2.4 4.8 2.4 8s-.9 6.2-2.4 8c-1.5-1.8-2.4-4.8-2.4-8s.9-6.2 2.4-8zM3.5 11h17v2h-17z"/></svg>
      www.korbalt.llc
    </li>
  </ul>
</section>

</body>
</html>
```